TOLVANE WEBSITE

We need a new look for our current website. Tolvane Fast Debt Recovery have been in business since 1977. We want our logo to remain the same however our current website is cluttered and we want something fresh, uncluttered, clean-line and easy to use. Our company colours are red, white and black.
We don't want pictures of people across the top of the page instead, we would like messages to appear (scrolling) across the top on a red background with white writing.
All that is required is from the designer to create a new look home page.
Good afternoon designers,
I have attached another page to the Tolvane Website profile. Could you please take a look and word towards creating something which incorporates the blue box.
I look forward to receiving your designs.
Thanks
Neil

```html
<!DOCTYPE html>
<html lang="en">
<head>
<meta charset="utf-8">
<title>Tolvane Fast Debt Recovery</title>
<link rel="stylesheet" href="https://fonts.googleapis.com/css2?family=Source+Sans+3:ital,wght@0,400;0,600;0,700;1,400;1,600;1,700&display=swap">
<style>
:root{
  --red:#8e2b2e;
  --red-deep:#5e1a1c;
  --red-bright:#a8383b;
  --ink:#3a3a3a;
  --text:#555;
  --muted:#777;
  --line:#cfcfcf;
  --band:#f4f4f4;
  --footer:#3a0b0c;
  --footer-deep:#230607;
  --footer-text:#d9c3c3;
  --white:#fff;
}
*{margin:0;padding:0;box-sizing:border-box}
html,body{width:1200px;height:2373px;overflow:hidden}
body{position:relative;background:var(--white);font-family:"Source Sans 3",sans-serif;color:var(--text)}
.abs{position:absolute}
a{color:inherit}

/* header */
.brand{left:191px;top:48px;font-size:48px;font-weight:700;color:var(--ink);letter-spacing:-1px;line-height:1}
.hotline{left:656px;top:80px;display:flex;align-items:center;gap:10px;font-size:26px;color:var(--ink)}
.hotline svg{width:34px;height:34px}
.divider{left:862px;top:86px;width:1px;height:26px;background:var(--line)}
.member{left:883px;top:80px;font-size:27px;color:#777;border-bottom:2px solid var(--red);line-height:1.1}
.member b{color:var(--red);font-weight:400}

/* hero banner */
.hero{left:0;top:132px;width:1200px;height:590px;background:linear-gradient(180deg,var(--red-deep) 0%,var(--red) 35%,var(--red-bright) 60%,var(--red) 85%,var(--red-deep) 100%)}
.nav{left:0;top:132px;width:1200px;height:54px;background:rgba(30,12,12,.72)}
.nav a{position:absolute;top:16px;font-size:17px;font-weight:600;color:var(--white);text-decoration:none}
.nav a.active{color:#e0787a}
.hero-shade{left:0;top:670px;width:1200px;height:52px;background:rgba(60,20,20,.35)}
.dots{left:561px;top:683px;width:107px;height:29px;border-radius:15px;background:var(--white);display:flex;justify-content:center;align-items:center;gap:7px}
.dots i{width:15px;height:15px;border-radius:50%;background:#ddd;border:1px solid #bbb}

/* section titles */
.section-title{left:164px;width:872px;display:flex;align-items:center;gap:22px;font-size:22px;font-weight:700;font-style:italic;color:var(--red)}
.section-title::before,.section-title::after{content:"";flex:1;height:1px;background:var(--line)}
.intro{left:164px;top:804px;width:872px;text-align:center;font-size:12.5px;font-style:italic;line-height:17px;color:var(--text)}
.more{font-size:13.5px;font-style:italic;font-weight:600;color:var(--ink);text-decoration:underline;text-align:center}

/* features */
.badge{width:98px;height:98px;border-radius:50%;display:flex;align-items:center;justify-content:center}
.badge svg{width:46px;height:46px}
.badge.red{background:var(--red)}
.badge.dark{background:var(--ink)}
.feature{width:420px;text-align:center}
.feature h3{font-size:22px;font-weight:600;color:var(--red);line-height:26px}
.feature h4{font-size:15px;font-style:italic;font-weight:400;color:var(--ink);margin-top:2px}
.feature p{font-size:12.5px;font-style:italic;line-height:17px;color:var(--text);margin:8px auto 0;width:380px}
.feature p em{color:var(--red)}
.feature .more{display:block;margin-top:14px}

/* quick buttons */
.quick{top:1476px;width:141px;height:50px;border:1px solid #ddd;border-radius:3px;box-shadow:0 2px 3px rgba(0,0,0,.12);background:var(--white);display:flex;align-items:center;justify-content:center;text-align:center;font-size:15px;line-height:17px;color:var(--red)}

/* contact band */
.band{left:0;top:1564px;width:1200px;height:280px;background:var(--band);border-top:1px solid #ccc;border-bottom:1px solid #ccc}
.action{width:220px;text-align:center}
.action .badge{margin:0 auto;border:5px solid var(--white);box-shadow:0 0 0 1px #ddd;position:relative}
.action .badge::after{content:"";position:absolute;left:40px;bottom:-12px;border:8px solid transparent;border-top-color:var(--white)}
.action h3{font-size:22px;font-weight:600;color:var(--red);margin-top:14px}
.action p{font-size:12.5px;font-style:italic;line-height:17px;color:var(--text);margin-top:6px}
.action .more{display:block;margin-top:12px}

/* offices */
.address{left:300px;top:1910px;width:600px;text-align:center;font-size:12.5px;font-style:italic;line-height:17px;color:var(--ink)}
.cities{left:150px;top:1972px;width:900px;display:flex;justify-content:center;gap:16px;font-size:12.5px;font-style:italic;color:var(--muted)}
.cities span{text-decoration:underline}

/* footer */
.footer{left:0;top:2026px;width:1200px;height:240px;background:var(--footer)}
.fcol{top:2055px;font-size:12.5px;line-height:16px;color:var(--footer-text)}
.fcol h5{font-size:12.5px;font-weight:600;color:var(--white);text-decoration:underline;margin-bottom:18px}
.legal{left:0;top:2266px;width:1200px;height:107px;background:var(--footer-deep)}
.copy{left:0;top:2284px;width:1200px;text-align:center;font-size:12px;color:var(--footer-text)}
.social{top:2312px;width:40px;height:40px;border-radius:50%;background:#8a4b4e}
</style>
</head>
<body>

<header>
  <div class="abs brand">TOLVANE</div>
  <div class="abs hotline">
    <svg viewBox="0 0 24 24"><path fill="#8e2b2e" d="M6.6 2.5l3 3.6-1.8 2.4c1.2 2.6 3.2 4.6 5.8 5.8l2.4-1.8 3.6 3-1.6 3.4C11 18.4 5.6 13 4.1 4.1z"/></svg>
    1800 555 203
  </div>
  <div class="abs divider"></div>
  <div class="abs member">Member <b>Login</b></div>
</header>

<section>
  <div class="abs hero" role="img" aria-label="Red banner slideshow: businessmen in suits holding umbrellas and document folders in the rain"></div>
  <nav class="abs nav">
    <a class="active" style="left:154px">Home</a>
    <a style="left:239px">About Us</a>
    <a style="left:346px">Rates</a>
    <a style="left:425px">Products &amp; Solutions</a>
    <a style="left:612px">Media Centre</a>
    <a style="left:746px">Careers</a>
    <a style="left:841px">Contact Us</a>
    <a style="left:958px">Client Login</a>
  </nav>
  <div class="abs hero-shade"></div>
  <div class="abs dots"><i></i><i></i><i></i><i></i></div>
</section>

<main>
  <h2 class="abs section-title" style="top:762px">Welcome to our site</h2>
  <p class="abs intro">Tolvane Fast Debt Recovery has been in business since 1977. We work on a NO RECOVERY - NO CHARGE basis and have over 44,000 clients Australia wide. Lorem ipsum dolor sit amet, consectetur adipisicing elit, sed do eiusmod tempor incididunt ut labore et dolore magna aliqua. Ut enim ad minim veniam, quis nostrud exercitation ullamco laboris nisi ut aliquip ex ea commodo consequat. Duis aute irure dolor in reprehenderit in voluptate velit esse cillum dolore eu fugiat nulla pariatur. Excepteur sint occaecat cupidatat non proident, sunt in culpa qui officia deserunt mollit anim id est laborum.</p>
  <a class="abs more" style="left:560px;top:884px;width:80px">More...</a>

  <div class="abs badge red" style="left:329px;top:932px"><svg viewBox="0 0 24 24"><path fill="#fff" d="M5 8h14l-1 13H6z"/><path fill="none" stroke="#fff" stroke-width="1.8" d="M9 10V6a3 3 0 016 0v4"/></svg></div>
  <div class="abs badge red" style="left:792px;top:932px"><svg viewBox="0 0 24 24"><circle cx="12" cy="8" r="4.5" fill="#fff"/><path fill="#fff" d="M3 21c0-5 4-8 9-8s9 3 9 8z"/></svg></div>
  <div class="abs feature" style="left:168px;top:1040px">
    <h3>What we do</h3><h4>we help your business</h4>
    <p>Lorem ipsum dolor sit amet, consectetur adipisicing elit, sed do eiusmod tempor incididunt ut labore et dolore magna aliqua. Ut enim ad minim veniam, quis nostrud exercitation ullamco laboris nisi ut aliquip ex ea commodo consequat.</p>
    <a class="more">More...</a>
  </div>
  <div class="abs feature" style="left:631px;top:1040px">
    <h3>Who we are</h3><h4>Debt collection specialists</h4>
    <p>Lorem ipsum dolor sit amet, consectetur adipisicing elit, sed do eiusmod tempor incididunt ut labore et dolore magna aliqua. Ut enim ad minim veniam, quis nostrud exercitation ullamco laboris nisi ut aliquip ex ea commodo consequat.</p>
    <a class="more">More...</a>
  </div>

  <div class="abs badge dark" style="left:329px;top:1215px"><svg viewBox="0 0 24 24"><text x="12" y="19.5" text-anchor="middle" font-family="Source Sans 3,sans-serif" font-weight="700" font-size="22" fill="#fff">$</text></svg></div>
  <div class="abs badge dark" style="left:792px;top:1215px"><svg viewBox="0 0 24 24"><rect x="4" y="4" width="16" height="5" rx="1" fill="#fff"/><rect x="4" y="11" width="16" height="5" rx="1" fill="#fff"/><path stroke="#fff" stroke-width="1.8" d="M12 16v4M6 20h12"/></svg></div>
  <div class="abs feature" style="left:168px;top:1323px">
    <h3>Our rates</h3>
    <p><em>Commision rates from 11%</em> and that is all you pay because our service is totally completed. Because we say our clients that if there 'NO RECOVERY - NO CHARGES'.</p>
    <a class="more">Check-out...</a>
  </div>
  <div class="abs feature" style="left:631px;top:1323px">
    <h3>Tolvane online</h3>
    <p><em>Self-send letters</em> commission free debt collection.<br>Write something more information about it, for your valuable customers to get more response from them.</p>
    <a class="more">Order Now...</a>
  </div>

  <a class="abs quick" style="left:152px">Harwell<br>Lawyers</a>
  <a class="abs quick" style="left:301px">Submit a debt</a>
  <a class="abs quick" style="left:450px">Corporate<br>clients</a>
  <a class="abs quick" style="left:600px">Small<br>business</a>
  <a class="abs quick" style="left:749px">Make a<br>payment</a>
  <a class="abs quick" style="left:898px">Forums</a>

  <section class="abs band"></section>
  <div class="abs action" style="left:166px;top:1599px">
    <div class="badge red"><svg viewBox="0 0 24 24"><circle cx="12" cy="7" r="4" fill="#fff"/><path fill="#fff" d="M4 21c0-5 3.5-8 8-8s8 3 8 8z"/><path fill="#8e2b2e" d="M11 13h2l.6 5-1.6 2-1.6-2z"/></svg></div>
    <h3>Need advice?</h3><p>Call us on our toll free No<br>1800 555 203</p><a class="more">Right Now...</a>
  </div>
  <div class="abs action" style="left:376px;top:1599px">
    <div class="badge dark"><svg viewBox="0 0 24 24"><path fill="#fff" d="M6.6 2.5l3 3.6-1.8 2.4c1.2 2.6 3.2 4.6 5.8 5.8l2.4-1.8 3.6 3-1.6 3.4C11 18.4 5.6 13 4.1 4.1z"/></svg></div>
    <h3>Callback</h3><p>Request a callback now<br>to know more.</p><a class="more">Right Now...</a>
  </div>
  <div class="abs action" style="left:597px;top:1599px">
    <div class="badge red"><svg viewBox="0 0 24 24"><rect x="5" y="4" width="14" height="17" rx="1.5" fill="none" stroke="#fff" stroke-width="1.8"/><rect x="9" y="2.5" width="6" height="3" fill="#fff"/><path stroke="#fff" stroke-width="1.6" d="M8 10h8M8 13.5h8M8 17h5"/></svg></div>
    <h3>Enquiry us</h3><p>Fill the enquiry form to get<br>more info.</p><a class="more">click Here...</a>
  </div>
  <div class="abs action" style="left:827px;top:1599px">
    <div class="badge dark"><svg viewBox="0 0 24 24"><rect x="3" y="6" width="18" height="12" fill="#fff"/><path fill="none" stroke="#3a3a3a" stroke-width="1.5" d="M3 6l9 7 9-7"/></svg></div>
    <h3>Info-pack</h3><p>Request free information<br>pack to know more.</p><a class="more">click Here...</a>
  </div>

  <h2 class="abs section-title" style="top:1872px">Head office &amp; branches</h2>
  <p class="abs address">14 Harlow Lane. Brennick. Victoria. 3190 (Melbourne)<br>Tel: 1800 555 203<br>Fax: (03) 9000 4120</p>
  <div class="abs cities"><span>Adelaide</span><span>Ballarat Cairns</span><span>Dubbo</span><span>Geelong</span><span>Launceston</span><span>Newcastle</span><span>Brisbane</span><span>Sydney</span><span>Wagga</span><span>Warrnambool</span></div>
</main>

<footer>
  <div class="abs footer"></div>
  <div class="abs fcol" style="left:163px;width:200px">
    <h5>Latest Newspaper Articles</h5>
    Limping to insolvency, Daily Ledger,<br>13/12/2012<br>Debt agreements: life saver or<br>problematic, Trade Pipeline,<br>12/12/2012<br>Overspending, a Xmas danager, Daily<br>Ledger - Online.,<br>07/12/2012<br>Silly Season Alert, Capital Gazette,<br>07/12/2012
  </div>
  <div class="abs fcol" style="left:419px;width:190px">
    <h5>More Links</h5>
    Debt Collection Agency<br>Why Should Choose Tolvane<br>Debt Collection Solutions<br>Submit Your Debt Online<br>Corporate Clients Solutions<br>Small Business Solutions
  </div>
  <div class="abs fcol" style="left:625px;width:210px">
    <h5>More Forms</h5>
    Free Sample &amp; Form<br>Free Sticker System Sample Credit<br>Application Form<br>Directors' Guarantee Form
  </div>
  <div class="abs fcol" style="left:847px;width:230px">
    <h5>Contact Us</h5>
    Contact Tolvane<br>Contact Debt Collection Experts on<br>1800 555 203<br>Enquire Now<br>Request a Call Back
  </div>
  <div class="abs legal"></div>
  <p class="abs copy">Copyright @ 2012, TOLVANE &nbsp;|&nbsp; Terms &amp; Privacy Policy</p>
  <span class="abs social" style="left:524px"></span>
  <span class="abs social" style="left:577px"></span>
  <span class="abs social" style="left:629px"></span>
</footer>

</body>
</html>
```